HomePage Design for Lumen Getaways - once-in-a-lifetime experiences for busy working people

Design a homepage for the Lumen Getaways (www.lumengetaways.example) website compatible with further web pages and the design briefing documents attached

LG HomePage Design Brief
We are seeking website HomePage designs incorporating our new Logo and colour scheme, for Lumen Getaways (www.lumengetaways.example) to go with the site functionality and wireframe ideas attached.
The website HomePage design needs to
• Incorporate and be consistent with the LG Logo and its colour scheme attached.
• Express the brand values of being inspirational, high quality, upscale, cultured, aspirational, and contemporary – even somewhat ‘hip’. Probably positioned somewhere between Harlow Pike (Deluxe Travel) and Green Walrus (Hip Travel) – see https://www.harlowpike.example and https://www.greenwalrus.example .
• Be instantly recognisable and different from other travel websites and instantly communicate the nature of the brand proposition and target customer base.
• Appeal to our core 25-55 affluent businesspeople demographic
• Work in the UK, US/Canada and Australia/NZ and ultimately in mainland Europe.
• Use fonts and colours that are easily reproduced online and compatible with nearly all browsers.
• Be part of a responsive website design, that can be used both on Desktops and laptops but also with tablets and mobile ‘phones (hence content not too wide across the page)
• Feature the strapline ‘Lumen Getaways in less than 7 Days’
• Work with the and wireframes and processes shown in the attached presentation – although intended as a guide only these features and processes all need to be incorporated into the HomePage.
• Make full use of high quality images and video to convey our brand proposition and products

Target Market(s)

25-55 affluent businesspeople

Industry/Entity Type

Travel Industry

Number of Pages Required

1 page

Font styles to use
Sans Serif

Colors
0455a3
00a88f

Requirements
Must have
• • Incorporate and be consistent with the LG Logo and its colour scheme attached.
• • Express the brand values of being inspirational, high quality, upscale, cultured, aspirational, and contemporary – even somewhat ‘hip’. Probably positioned somewhere between Harlow Pike (Deluxe Travel) and Green Walrus (Hip Travel) – see https://www.harlowpike.example and https://www.greenwalrus.example .
• • Be instantly recognisable and different from other travel websites and instantly communicate the nature of the brand proposition and target customer base.
• • Appeal to our core 25-55 affluent businesspeople demographic
• • Be part of a responsive website design, that can be used both on Desktops and laptops but also with tablets and mobile ‘phones (hence content not too wide across the page)
• • Feature the strapline ‘Lumen Getaways in less than 7 Days’
• • Work with the and wireframes and processes shown in the attached presentation – although intended as a guide only these features and processes all need to be incorporated into the HomePage.
• • Make full use of high quality images and video to convey our brand proposition and products
• Colours as per Logo not as shown below
Nice to have
• • Work in the UK, US/Canada and Australia/NZ and ultimately in mainland Europe.
Should not have
• Must not be cheap or mass-market, nor excessively "stuffy or luxury-orientated"

```html
<!DOCTYPE html>
<html lang="en">
<head>
<meta charset="utf-8">
<title>Lumen Getaways — Home</title>
<link rel="stylesheet" href="https://fonts.googleapis.com/css2?family=Open+Sans:wght@400;600;700;800&family=Montserrat:wght@400;600;700&display=swap">
<style>
:root{
  --navy:#232d6b;
  --navy-deep:#1b2150;
  --navy-night:#161b45;
  --blue:#2b3f9e;
  --blue-mid:#1f3190;
  --green:#6cc644;
  --green-bright:#42c34d;
  --green-pale:#8fe068;
  --green-dark:#1d5e3a;
  --grey-bg:#ececec;
  --grey-line:#d5d5d5;
  --text:#4c4c4c;
  --muted:#8a8a8a;
  --white:#ffffff;
}
*{box-sizing:border-box;margin:0;padding:0}
html,body{width:1200px;height:3488px;overflow:hidden}
body{font-family:"Open Sans",Arial,sans-serif;color:var(--text);background:var(--white);font-size:12px}
.wrap{width:1028px;margin:0 auto;position:relative;height:100%}

/* top bar */
.topbar{height:22px;background:var(--navy-deep);color:#b9bfe0;font-size:10px}
.topbar .wrap{display:flex;align-items:center;justify-content:space-between}
.plan-tab{position:absolute;left:50%;top:0;transform:translateX(-50%);background:var(--green-dark);color:var(--white);font-weight:700;font-size:11px;letter-spacing:.5px;height:22px;line-height:22px;padding:0 26px}
.follow{display:flex;align-items:center;gap:6px}
.follow i{width:9px;height:9px;border-radius:50%;background:#8c93c2;display:block}

/* header */
.header{height:158px}
.header .wrap{display:flex;align-items:center}
.partners-top{display:flex;gap:26px;align-items:center;width:300px}
.partners-top span{font-family:"Open Sans",sans-serif;font-size:17px;color:#b4b4b4;font-weight:400}
.brand{position:absolute;left:50%;top:18px;transform:translateX(-50%);text-align:center}
.brand-mark{display:flex;align-items:center;justify-content:center;gap:8px}
.brand-mark i{width:44px;height:44px;border-radius:50%;background:var(--green-dark);display:block}
.brand-name{font-size:22px;font-weight:800;color:var(--green-dark);letter-spacing:1px;text-transform:uppercase;margin-top:8px}
.brand-sub{font-size:9px;color:var(--green-dark);letter-spacing:3px;font-weight:600}
.brand-tag{font-size:13px;color:var(--green);font-weight:700;letter-spacing:.6px;margin-top:18px;white-space:nowrap}
.phone{position:absolute;right:0;top:43px;width:235px;height:42px;background:#e6e6e6;display:flex;align-items:center;justify-content:space-between;padding-left:20px;font-size:17px;font-weight:700;color:#333}
.phone b{width:42px;height:42px;background:var(--green-dark);display:flex;align-items:center;justify-content:center}

/* nav */
.nav{height:36px;border-top:1px solid #e3e3e3;border-bottom:1px solid #e3e3e3}
.nav .wrap{display:flex;align-items:center}
.nav a{font-size:10px;font-weight:600;color:#666;text-decoration:none;padding:0 18px;height:34px;line-height:34px;text-transform:uppercase}
.nav a.active{background:#e2e2e2;color:var(--navy);padding:0 24px}
.search{position:absolute;right:0;top:-1px;display:flex;height:36px}
.search span{width:194px;background:#e9e9e9;font-size:10px;color:#888;line-height:36px;padding-left:14px}
.search b{width:36px;background:var(--navy);display:flex;align-items:center;justify-content:center}

/* hero */
.hero{height:529px;position:relative;background:linear-gradient(180deg,#2f5f4a 0%,#3a5e6e 35%,#3b6f86 60%,#2b3d66 100%)}
.hero::before{content:"";position:absolute;inset:0;background:linear-gradient(90deg,rgba(30,110,80,.35),rgba(150,40,110,.35) 60%,rgba(40,50,120,.35))}
.hero .wrap{z-index:1}
.hero-copy{position:absolute;left:0;top:156px;width:400px;color:var(--white)}
.hero-copy h1{font-family:"Montserrat",sans-serif;font-size:25px;line-height:1.18;font-weight:700}
.hero-copy p{font-size:14px;line-height:1.4;margin-top:10px;text-transform:uppercase;font-weight:600}
.btn-dark{display:inline-block;margin-top:20px;background:#151a2e;color:var(--white);font-size:11px;font-weight:700;padding:9px 22px;letter-spacing:.5px}
.hero-arrow{position:absolute;top:256px;color:var(--white);font-size:26px;line-height:1}
.hero-arrow.l{left:-50px}.hero-arrow.r{right:-50px}

/* tabs */
.tabs{height:41px;display:flex}
.tabs a{flex:1;display:flex;align-items:center;justify-content:center;color:var(--white);font-size:12px;font-weight:600;text-decoration:none;text-transform:uppercase}
.t1{background:var(--navy-deep)}.t2{background:var(--blue)}.t3{background:var(--blue-mid)}.t4{background:var(--navy-night)}
.t5{background:var(--green)}.t6{background:var(--green-bright)}.t7{background:var(--green-pale);color:#d8f7c8!important}.t8{background:var(--green-dark)}

/* features */
.features{height:442px;background:linear-gradient(180deg,#f0f0f0,#e6e6e6)}
.features .wrap{display:flex}
.feature{flex:1;text-align:center;padding:19px 40px 0;position:relative}
.feature+.feature::before{content:"";position:absolute;left:0;top:51px;height:349px;border-left:1px solid var(--grey-line)}
.feature .thumb{width:128px;height:128px;border-radius:50%;margin:0 auto;border:3px solid var(--white)}
.feature h3{font-family:"Montserrat",sans-serif;font-size:17px;font-weight:600;color:var(--navy);margin-top:80px;text-transform:uppercase}
.feature p{font-size:10px;line-height:1.45;color:var(--muted);margin-top:8px;height:62px}
.btn-navy{display:inline-block;background:var(--navy);color:var(--white);font-size:10px;font-weight:600;padding:6px 16px;margin-top:14px}

/* welcome */
.welcome{height:235px;text-align:center}
.welcome h2{font-family:"Montserrat",sans-serif;font-size:22px;font-weight:400;color:#777;padding-top:62px;letter-spacing:.5px}
.welcome h2 strong{color:var(--navy);font-weight:600}
.welcome p{width:860px;margin:18px auto 0;font-size:12.5px;line-height:1.75;color:#7a7a7a}

/* grid */
.grid{height:1028px}
.tiles{width:1028px;margin:0 auto;display:grid;grid-template-columns:repeat(4,257px);grid-template-rows:repeat(4,257px)}
.tile{position:relative;padding:20px 18px;color:var(--white)}
.tile h4{font-size:14px;line-height:1.25;font-weight:700;margin-bottom:8px}
.tile p{font-size:9.6px;line-height:1.38;font-weight:600}
.tile .more{position:absolute;left:18px;bottom:18px;width:30px;border-top:1px solid rgba(255,255,255,.8)}
.tile-navy{background:var(--navy)}
.tile-green{background:var(--green)}
.tile-navy.point-l::before,.tile-green.point-l::before{content:"";position:absolute;left:-12px;top:40px;border:12px solid transparent;border-left:0}
.tile-navy.point-l::before{border-right-color:var(--navy)}
.tile-green.point-l::before{border-right-color:var(--green)}
.tile-green.point-r::after,.tile-navy.point-r::after{content:"";position:absolute;right:-12px;top:40px;border:12px solid transparent;border-right:0;z-index:2}
.tile-green.point-r::after{border-left-color:var(--green)}
.tile-navy.point-r::after{border-left-color:var(--navy)}
.ph{display:block}
.zoom{position:absolute;left:50%;top:50%;transform:translate(-50%,-50%);width:44px;height:44px;border-radius:50%;background:rgba(30,40,60,.75);display:flex;align-items:center;justify-content:center}
.video{grid-column:span 2;position:relative}
.play{position:absolute;left:50%;top:50%;transform:translate(-50%,-50%)}

/* top picks */
.picks{height:433px}
.picks h2{text-align:center;font-family:"Montserrat",sans-serif;font-size:17px;font-weight:600;color:var(--navy);padding-top:45px}
.cards{display:flex;gap:26px;margin-top:27px}
.card{width:238px;height:275px;background:#eef0f3;position:relative}
.card .ph{height:156px}
.card h3{font-size:15px;font-weight:400;color:#444;text-align:center;margin-top:14px}
.card p{font-size:10px;line-height:1.35;color:#8b8b8b;padding:4px 18px 0}
.card-bar{position:absolute;left:0;right:0;bottom:0;height:30px;background:var(--navy);display:flex;align-items:center;justify-content:space-between;color:var(--white);font-size:11px;font-weight:600;padding-left:16px}
.card-bar b{width:30px;height:30px;background:var(--green);display:flex;align-items:center;justify-content:center}

/* accreditation */
.accred{height:111px;background:#efefef}
.accred .wrap{display:flex;align-items:center;justify-content:space-between;padding:0 60px}
.badge{background:#c9c9c9}
.accred-arrow{position:absolute;top:40px;color:#b5b5b5;font-size:22px}

/* newsletter */
.newsletter{height:124px;background:var(--green)}
.newsletter .wrap{display:flex;align-items:center;gap:20px}
.newsletter h3{color:var(--white);font-size:17px;line-height:1.15;font-weight:600;text-transform:uppercase;width:160px}
.field{background:var(--white);height:38px;font-size:12px;color:#555;padding-left:14px;line-height:38px;width:320px}
.btn-sub{background:var(--navy);color:var(--white);font-size:11px;font-weight:700;height:38px;line-height:38px;padding:0 40px}

/* footer */
.footer{height:226px;background:var(--navy)}
.footer .wrap{display:flex;padding-top:66px}
.footer .col{width:263px}
.footer h4{color:var(--white);font-size:12px;font-weight:600;text-transform:uppercase;letter-spacing:.3px}
.footer ul{list-style:none;margin-top:18px}
.footer li{color:#a7acd0;font-size:10px;line-height:2.5}
.footer li::before{content:"› ";color:#7f86b8}
.bottom{height:103px;background:var(--navy-night);color:#aeb3d6;font-size:10px}
.bottom .wrap{display:flex;justify-content:space-between;padding-top:40px;line-height:1.5}
.bottom .right{text-align:right}
</style>
</head>
<body>

<div class="topbar"><div class="wrap">
  <span>E-mail: info@lumengetaways.example</span>
  <span class="plan-tab">LET'S PLAN YOUR TRIP</span>
  <span class="follow">Follow us : <i></i><i></i><i></i><i></i><i></i></span>
</div></div>

<header class="header"><div class="wrap">
  <div class="partners-top"><span>Harlow Pike</span><span>Green Walrus</span></div>
  <div class="brand">
    <div class="brand-mark"><i></i></div>
    <div class="brand-name">Lumen Getaways</div>
    <div class="brand-sub">IN LESS THAN 7 DAYS</div>
    <div class="brand-tag">'CAYMAN'S PREMIER ADVENTURE AND RENTAL COMPANY'</div>
  </div>
  <div class="phone">+44 000 000 0000
    <b><svg width="20" height="20" viewBox="0 0 24 24"><path fill="#fff" d="M6.6 10.8a15 15 0 0 0 6.6 6.6l2.2-2.2a1 1 0 0 1 1-.25 11.4 11.4 0 0 0 3.6.57 1 1 0 0 1 1 1V20a1 1 0 0 1-1 1A17 17 0 0 1 3 4a1 1 0 0 1 1-1h3.5a1 1 0 0 1 1 1c0 1.25.2 2.45.57 3.57a1 1 0 0 1-.25 1z"/></svg></b>
  </div>
</div></header>

<nav class="nav"><div class="wrap">
  <a class="active">Home Page</a><a>Rental Gear ▾</a><a>Adventure Map ▾</a><a>Tours</a><a>Photo Gallery</a><a>Contact Us</a>
  <div class="search"><span>SEARCH</span><b><svg width="16" height="16" viewBox="0 0 24 24"><circle cx="10" cy="10" r="6.5" fill="none" stroke="#fff" stroke-width="2.5"/><path d="M15 15l6 6" stroke="#fff" stroke-width="2.5"/></svg></b></div>
</div></nav>

<section class="hero" role="img" aria-label="Two women on a paddle board on calm turquoise sea at sunset">
  <div class="wrap">
    <div class="hero-copy">
      <h1>LUMEN GETAWAYS<br>IN LESS THAN 7 DAYS!</h1>
      <p>Get onboard now for the launch of our brand new online platform offering once-in-a-lifetime experiences for busy people</p>
      <span class="btn-dark">EXPLORE NOW &nbsp;›</span>
    </div>
    <span class="hero-arrow l">‹</span><span class="hero-arrow r">›</span>
  </div>
</section>

<div class="tabs">
  <a class="t1">Destinations</a><a class="t2">Experiences</a><a class="t3">Trips by Month</a><a class="t4">Topical Now</a>
  <a class="t5">Tailored</a><a class="t6">Pioneers Club</a><a class="t7">Client Log In</a><a class="t8">Blogs &amp; Reviews</a>
</div>

<section class="features"><div class="wrap">
  <div class="feature">
    <div class="thumb" role="img" aria-label="People in a kayak on clear blue water" style="background:radial-gradient(circle,#4fc3d8,#1f8fb3)"></div>
    <h3>Exploration</h3>
    <p>Rent everything you need to get outside and explore the island on your own terms. Snorkel the Kittiwake, check out the bioluminescence and much more with your own gear!</p>
    <span class="btn-navy">READ MORE</span>
  </div>
  <div class="feature">
    <div class="thumb" role="img" aria-label="Kayakers seen from above on turquoise water" style="background:radial-gradient(circle,#3fb7b0,#1b7f88);position:relative"><span class="zoom" style="width:40px;height:40px"><svg width="16" height="16" viewBox="0 0 24 24"><circle cx="10" cy="10" r="6.5" fill="none" stroke="#fff" stroke-width="2.5"/><path d="M15 15l6 6" stroke="#fff" stroke-width="2.5"/></svg></span></div>
    <h3>Relaxation</h3>
    <p>We will come straight to your resort or condo and set everything up for you and your family to enjoy. Our kayaks and paddle boards on the beautiful calm waters off Seven Mile Beach.</p>
    <span class="btn-navy">READ MORE</span>
  </div>
  <div class="feature">
    <div class="thumb" role="img" aria-label="Placeholder stamp image" style="background:#f4f4f4"></div>
    <h3>Education</h3>
    <p>We love sharing our knowledge on Cayman's history and the island's extraordinary marine life. We'll also teach you everything you need to find those secluded spots on your adventures.</p>
    <span class="btn-navy">READ MORE</span>
  </div>
</div></section>

<section class="welcome">
  <h2>WELCOME TO <strong>BRIGHTWAVE CAYMAN!</strong></h2>
  <p>We love having the freedom to explore when traveling and we bet you do to! We are Grand Cayman's premier rental company, offering everything you need to make the most of your vacation. Our website serves as a great starting point to help you prepare for your vacation here in Cayman. We feature a huge selection of adventures on our interactive map with tons of useful information, pictures and directions. Our adventure map is the perfect guide to all our great spots to check out here in Cayman.</p>
</section>

<section class="grid"><div class="tiles">
  <div class="ph" role="img" aria-label="Aerial view of kayakers on turquoise shallows" style="background:linear-gradient(135deg,#58c7d0,#1e8ea6);position:relative"><span class="zoom"><svg width="18" height="18" viewBox="0 0 24 24"><circle cx="10" cy="10" r="6.5" fill="none" stroke="#fff" stroke-width="2.5"/><path d="M15 15l6 6" stroke="#fff" stroke-width="2.5"/></svg></span></div>
  <div class="tile tile-navy point-l"><h4>Your one stop shop for all the rentals you needhere in Cayman!</h4><p>We have a huge array of fun toys and equipment for you to enjoy. Whether it's for exploring or relaxing, we have all the equipment you need to make the most of your trip here in Cayman. Need something that we don't stock, just ask and we'll do everything we can to get you the gear you need!</p><span class="more"></span></div>
  <div class="ph" role="img" aria-label="Illustrated map of Grand Cayman" style="background:linear-gradient(160deg,#8fd3e8,#5cb8d6 55%,#9ccf7a)"></div>
  <div class="tile tile-green point-l"><h4>Check out our interactive map of Cayman!</h4><p>You won't find any tourist traps on our map! We're all about getting off the beaten path and finding those unique spots and natural wonders to explore. Get our expert advice on which adventures are best for you and how to tackle them!</p><span class="more"></span></div>

  <div class="tile tile-green point-r"><h4>Enjoy Complete freedom to explore.</h4><p>Inflatable kayaks have revolutionized the way kayak exploration is done in a way never before. Our kayaks give you the freedom to explore Cayman's most secluded locations and snorkel those hard to reach spots. Our kayaks are light, comfortable and easy to use.</p><span class="more"></span></div>
  <div class="ph" role="img" aria-label="Two women paddling a blue kayak on clear water" style="background:linear-gradient(180deg,#8ecfe0,#4fa9c4 60%,#c9e4e6)"></div>
  <div class="tile tile-navy point-r"><h4>There's no easier way to get around the island</h4><p>What better way is there to explore the island other than to rent a bike and go? Our mountain bikes are perfect for those interested on heading out on a full day adventure. If you're looking for something more casual, renting a cruiser is perfect to get around the Seven Mile Beach area. Use our map to help guide you to all our suggested locations to explore!</p><span class="more"></span></div>
  <div class="ph" role="img" aria-label="Two red beach cruiser bikes parked by the sea" style="background:linear-gradient(180deg,#9fd4ea,#6fbcd9 55%,#d9cdb2)"></div>

  <div class="ph" role="img" aria-label="Person sitting on a rocky cliff at dusk" style="background:linear-gradient(180deg,#4a5c7c,#7a6a78 50%,#6b3c2e)"></div>
  <div class="tile tile-navy point-l"><h4>We want to be your personal concierge and help you to plan out your trip!</h4><p>When we come to deliver your equipment, we teach you everything you need to know about the island including the best hidden spots, best restaurants &amp; bars to eat &amp; drink and anything else you might be curious about. Please don't hesitate to contact us for any and all of your vacation questions. We are happy to help!</p><span class="more"></span></div>
  <div class="ph" role="img" aria-label="Floating hammock boat with family on green water" style="background:linear-gradient(160deg,#4fa49a,#2c7f74 60%,#5fb0a4)"></div>
  <div class="tile tile-green point-l"><h4>Is it a boat? is it a whale? ... It's a Floatlounge!</h4><p>Easily one of the coolest inventions we've ever come across, the Floatlounge is a versatile toy the whole family can enjoy together. Spend the day cruising along Seven Mile Beach in style as you bar hop with your clan. Better still, bring a cooler on board and put the kids to work paddling as you relax in your hammock on the crystal clear waters!</p><span class="more"></span></div>

  <div class="tile tile-green point-r"><h4>A new way to Snorkel!</h4><p>Our full face snorkel masks are easy to use, making them perfect for kids and beginners. You simply put the mask on and breathe as you usually would. There's no need to get used to breathing from your mouth and you don't experience a sore jaw from having to hold the mouth piece in place. Just ask and we'll bring one along for you to try!</p><span class="more"></span></div>
  <div class="ph" role="img" aria-label="Snorkeller in a full face mask underwater" style="background:linear-gradient(180deg,#6fd0dc,#2fa2c0 60%,#c86fa8)"></div>
  <div class="video" role="img" aria-label="Video still of a traveller overlooking mountain ruins" style="background:linear-gradient(160deg,#8e9ba3,#5d6f5f 55%,#3f4a3a)">
    <svg class="play" width="64" height="64" viewBox="0 0 64 64"><circle cx="32" cy="32" r="29" fill="none" stroke="#fff" stroke-width="3"/><path d="M26 20l18 12-18 12z" fill="#fff"/></svg>
  </div>
</div></section>

<section class="picks"><div class="wrap">
  <h2>Our Adventure Top-Picks</h2>
  <div class="cards">
    <div class="card"><div class="ph" role="img" aria-label="Glowing blue bioluminescent bay at night" style="background:linear-gradient(180deg,#0b1838,#123a6e 60%,#2d7fc0)"></div><h3>Bio Bay Main</h3><p>Lorem ipsum dolor sit amet, consectetuer adipiscing elit. Aenean commodo ligula eget dolor. Aenean massa.</p><div class="card-bar">Read More+<b><svg width="12" height="16" viewBox="0 0 12 16"><path d="M6 0a6 6 0 0 1 6 6c0 4.5-6 10-6 10S0 10.5 0 6a6 6 0 0 1 6-6z" fill="#fff"/><circle cx="6" cy="6" r="2.2" fill="#6cc644"/></svg></b></div></div>
    <div class="card"><div class="ph" role="img" aria-label="Underwater shipwreck in clear blue water" style="background:linear-gradient(180deg,#3fb6d4,#1b7fa8)"></div><h3>Kittiwake</h3><p>Lorem ipsum dolor sit amet, consectetuer adipiscing elit. Aenean commodo ligula eget dolor. Aenean massa.</p><div class="card-bar">Read More+<b><svg width="12" height="16" viewBox="0 0 12 16"><path d="M6 0a6 6 0 0 1 6 6c0 4.5-6 10-6 10S0 10.5 0 6a6 6 0 0 1 6-6z" fill="#fff"/><circle cx="6" cy="6" r="2.2" fill="#6cc644"/></svg></b></div></div>
    <div class="card"><div class="ph" role="img" aria-label="Aerial view of a small sandy cay" style="background:linear-gradient(180deg,#2a8fb8,#4ec1c9 55%,#e8e2c8)"></div><h3>Sand Cay Island</h3><p>Lorem ipsum dolor sit amet, consectetuer adipiscing elit. Aenean commodo ligula eget dolor. Aenean massa.</p><div class="card-bar">Read More+<b><svg width="12" height="16" viewBox="0 0 12 16"><path d="M6 0a6 6 0 0 1 6 6c0 4.5-6 10-6 10S0 10.5 0 6a6 6 0 0 1 6-6z" fill="#fff"/><circle cx="6" cy="6" r="2.2" fill="#6cc644"/></svg></b></div></div>
    <div class="card"><div class="ph" role="img" aria-label="Stingrays gliding over a sandy sea floor" style="background:linear-gradient(180deg,#4a9bb0,#3a8a9e 60%,#b9b7a0)"></div><h3>Stingray City</h3><p>Lorem ipsum dolor sit amet, consectetuer adipiscing elit. Aenean commodo ligula eget dolor. Aenean massa.</p><div class="card-bar">Read More+<b><svg width="12" height="16" viewBox="0 0 12 16"><path d="M6 0a6 6 0 0 1 6 6c0 4.5-6 10-6 10S0 10.5 0 6a6 6 0 0 1 6-6z" fill="#fff"/><circle cx="6" cy="6" r="2.2" fill="#6cc644"/></svg></b></div></div>
  </div>
</div></section>

<section class="accred"><div class="wrap">
  <span class="accred-arrow" style="left:0">‹</span>
  <span class="badge" style="width:74px;height:22px"></span>
  <span class="badge" style="width:62px;height:26px"></span>
  <span class="badge" style="width:130px;height:22px"></span>
  <span class="badge" style="width:60px;height:42px"></span>
  <span class="badge" style="width:52px;height:52px;border-radius:50%"></span>
  <span class="badge" style="width:72px;height:42px"></span>
  <span class="badge" style="width:104px;height:30px"></span>
  <span class="accred-arrow" style="right:0">›</span>
</div></section>

<section class="newsletter"><div class="wrap">
  <svg width="54" height="46" viewBox="0 0 54 46"><path d="M3 18L27 3l24 15v25H3z" fill="none" stroke="#1d5e3a" stroke-width="3"/><path d="M3 18l24 15 24-15" fill="none" stroke="#1d5e3a" stroke-width="3"/></svg>
  <h3>Subscribe our Newslewtter</h3>
  <div class="field">Full Name</div>
  <div class="field">Email Address</div>
  <div class="btn-sub">SUBSCRIBE</div>
</div></section>

<footer class="footer"><div class="wrap">
  <div class="col"><h4>About Us</h4><ul><li>Our Partners</li><li>Newsletter</li><li>FAQs</li></ul></div>
  <div class="col"><h4>Contacts Us</h4><ul><li>Booking Conditions</li><li>Privacy &amp; Cookies</li><li>Terms of Use</li></ul></div>
  <div class="col"><h4>Financial Protection</h4><ul><li>Travel Insurance</li><li>Visas</li><li>Travel Advice</li></ul></div>
  <div class="col"><h4>Group Bookings</h4><ul><li>Tailor-Made &amp; Extra Nights</li><li>Booking Flights</li><li>Careers with LG</li></ul></div>
</div></footer>

<div class="bottom"><div class="wrap">
  <div>LG Protecting wildlife &amp; animals, and supporting local communities<br>Press Room</div>
  <div class="right">lumen getaways<br>CoCopyright © 2017. All Rights Reserved.</div>
</div></div>

</body>
</html>
```